Web design for construction/ handyman company. We are a new company and trying to brand ourselves.

We have a logo with a character already in place and want a user friendly and simple site. I'm attaching our logo designs with our Crocodile character to get an idea of our logo. We want people to remember us and our site. The name we chose was so we could use a logo with a character. Our name is Pelican Builders LLC.

Target Market(s)

New clients

Industry/Entity Type

Contractor

Coding

Coded - Design and coding required

Number of Pages Required

4 page

Font styles to use
Sans Serif

Requirements
Must have
• About Us Page, What we do (not sure what to call this), Contact Us, Home Page. Would like the same colors as on our business card designs to be used on the website.
Nice to have
• We eventually want a project page to add photos of projects but thats not necessary now. Would be nice to use the crocodile theme, hammer or something similar somehow in the page names or clicks.

```html
<!DOCTYPE html>
<html lang="en">
<head>
<meta charset="utf-8">
<title>Pelican Builders LLC</title>
<link href="https://fonts.googleapis.com/css2?family=Open+Sans:wght@400;600;700;800&display=swap" rel="stylesheet">
<style>
:root{
  --blue:#0d4f8e;
  --green:#2f9a2a;
  --ink:#333;
  --muted:#888;
  --line:#e3e3e3;
  --panel:#f1f1f1;
  --white:#fff;
}
*{box-sizing:border-box;margin:0;padding:0}
html,body{width:1200px;height:2664px;overflow:hidden;background:var(--white);font-family:'Open Sans',Arial,sans-serif;color:var(--ink)}
.page{position:relative;width:1200px;height:2664px}
.header{position:absolute;top:0;left:0;width:1200px;height:132px}
.brand{position:absolute;left:96px;top:30px;display:flex;align-items:center;gap:12px}
.brand-mark{width:44px;height:44px;background:var(--green)}
.brand-name{font-size:26px;font-weight:800;color:var(--blue);line-height:1.05}
.header-phone{position:absolute;right:142px;top:26px;font-size:17px;font-weight:600;color:var(--blue)}
.header-dot{position:absolute;right:100px;top:22px;width:28px;height:28px;border-radius:50%;background:var(--green)}
.nav{position:absolute;right:100px;top:90px;display:flex;gap:34px;font-size:15px}
.nav a{color:var(--ink);text-decoration:none}
.nav a.active{color:var(--blue);font-weight:700}
.hero{position:absolute;top:132px;left:0;width:1200px;height:556px;background:linear-gradient(100deg,#c8d6e2 0%,#eef3f7 40%,#dbe4ea 70%,#b9c6cf 100%)}
.hero-arrow{position:absolute;top:260px;width:26px;height:26px;border-radius:50%;background:rgba(255,255,255,.7)}
.strip{position:absolute;top:688px;left:0;width:1200px;height:94px;background:var(--blue)}
.strip p{position:absolute;left:160px;top:32px;width:600px;font-size:20px;line-height:30px;color:var(--white);font-weight:600;white-space:nowrap}
.btn{display:inline-block;color:var(--white);font-size:15px;font-weight:600;text-align:center;border-radius:3px}
.btn-green{background:var(--green)}
.btn-blue{background:var(--blue)}
.strip .btn{position:absolute;left:800px;top:24px;width:160px;height:46px;line-height:46px}
.welcome{position:absolute;top:782px;left:0;width:1200px;text-align:center}
.section-title{font-size:38px;font-weight:700;color:var(--blue);letter-spacing:1px;line-height:1.3}
.welcome .section-title{margin-top:28px}
.rule{width:70px;height:3px;background:var(--green);margin:10px auto 0}
.welcome-text{width:1000px;margin:20px auto 0;font-size:14px;line-height:24px;color:var(--muted)}
.welcome-actions{margin-top:20px;display:flex;justify-content:center;gap:16px}
.welcome-actions .btn{width:120px;height:42px;line-height:42px;font-size:14px}
.projects{position:absolute;top:1076px;left:0;width:1200px;text-align:center}
.eyebrow{font-size:14px;line-height:20px;color:var(--muted);letter-spacing:2px}
.projects .section-title{font-size:34px;margin-top:2px}
.filters{display:flex;justify-content:center;gap:36px;margin-top:22px;font-size:13px;font-weight:600;color:var(--muted);border-bottom:1px solid var(--line);width:820px;margin-left:190px;padding-bottom:12px}
.filters span.active{color:var(--blue);border-bottom:3px solid var(--blue);padding-bottom:9px}
.grid{position:absolute;left:100px;width:1000px;display:grid;gap:20px}
.grid-two{top:1232px;grid-template-columns:1fr 1fr}
.grid-three{top:1664px;grid-template-columns:1fr 1fr 1fr}
.photo{width:100%}
.grid-two .photo{height:330px}
.grid-three .photo{height:250px}
.card-title{margin-top:22px;font-size:13px;font-weight:700;color:var(--ink);text-align:center}
.card-sub{margin-top:6px;font-size:12px;color:var(--muted);text-align:center;padding-bottom:14px;border-bottom:1px solid var(--line);width:60%;margin-left:20%}
.view-all{position:absolute;top:2034px;left:518px;width:164px;height:44px;line-height:44px}
.contact{position:absolute;top:2110px;left:0;width:1200px;height:510px;background:var(--panel);text-align:center}
.contact .section-title{font-size:34px;margin-top:30px}
.contact-text{width:760px;margin:20px auto 0;font-size:14px;line-height:22px;color:var(--muted)}
.details{position:absolute;left:176px;top:170px;text-align:left}
.details h4{font-size:14px;font-weight:600;letter-spacing:2px;color:var(--muted);margin-top:22px}
.details h4:first-child{margin-top:0}
.details p{font-size:14px;line-height:20px;color:var(--ink)}
.form{position:absolute;left:456px;top:158px;width:560px;height:150px;background:#e2e2e2}
.field{position:absolute;background:var(--white);height:30px;font-size:11px;color:var(--muted);text-align:left;padding:8px 10px}
.form .btn{position:absolute;left:402px;top:112px;width:118px;height:30px;line-height:30px;font-size:12px}
.form-note{position:absolute;left:456px;top:322px;font-size:12px;color:var(--muted)}
.footer{position:absolute;top:2620px;left:0;width:1200px;height:44px;background:var(--blue)}
.footer p{position:absolute;left:100px;top:13px;font-size:12px;color:#d7e3ef}
.social{position:absolute;right:100px;top:11px;display:flex;gap:8px}
.social span{width:22px;height:22px;border-radius:50%;background:#e5492f}
.social span:nth-child(2){background:#2f9fd6}
.social span:nth-child(3){background:#c1272d}
.social span:nth-child(4){background:#3b5b98}
</style>
</head>
<body>
<div class="page">
  <header class="header">
    <div class="brand"><span class="brand-mark"></span><span class="brand-name">Pelican Builders LLC</span></div>
    <div class="header-phone">(555) 014-2368</div>
    <span class="header-dot"></span>
    <nav class="nav">
      <a class="active" href="#">Home</a><a href="#">About us</a><a href="#">What we do</a><a href="#">Pricing</a><a href="#">Contact us</a>
    </nav>
  </header>

  <section class="hero" role="img" aria-label="Construction team reviewing blueprints with hard hat and glasses on the desk">
    <span class="hero-arrow" style="left:10px"></span>
    <span class="hero-arrow" style="right:10px"></span>
  </section>

  <section class="strip">
    <p>Lorem ipsum dolor sit amet, consectetur adipiscing elit</p>
    <span class="btn btn-green">Contact Now</span>
  </section>

  <section class="welcome">
    <h2 class="section-title">WELCOME</h2>
    <div class="rule"></div>
    <p class="welcome-text">Lorem ipsum dolor sit amet, consectetur adipiscing elit. Nullam tempor magna nec lacus luctus, vitae aliquet nisi posuere. Integer sed vestibulum risus, sed finibus nisl. Curabitur eget orci vel lacus pulvinar maximus. Praesent dictum felis at sem pharetra, id dictum ligula porta. Donec rutrum tellus sed ultricies sagittis. Morbi vulputate eros ac enim ullamcorper, in varius arcu semper. Vivamus viverra lectus a nisi condimentum, non iaculis velit tempus. Aliquam erat volutpat, sed sodales quam.</p>
    <div class="welcome-actions"><span class="btn btn-blue">Read More</span><span class="btn btn-green">View Works</span></div>
  </section>

  <section class="projects">
    <p class="eyebrow">AWESOME WORKS OF US</p>
    <h2 class="section-title">LATEST PROJECTS</h2>
    <div class="filters"><span class="active">ALL</span><span>COMMERCIAL</span><span>RESIDENTIAL</span><span>INTERIOR WORKS</span><span>EXTERIOR WORKS</span></div>
  </section>

  <div class="grid grid-two">
    <div><div class="photo" role="img" aria-label="Worker on a concrete building site" style="background:linear-gradient(160deg,#cfe0ee,#8a96a0)"></div><p class="card-title">DIAM NUMMY NOLESTIE MOLESTIE</p><p class="card-sub">Commercial</p></div>
    <div><div class="photo" role="img" aria-label="Timber house frame under a blue sky" style="background:linear-gradient(170deg,#6fa6d8,#c9a27a)"></div><p class="card-title">DIAM NUMMY NOLESTIE MOLESTIE</p><p class="card-sub">Residential</p></div>
  </div>

  <div class="grid grid-three">
    <div><div class="photo" role="img" aria-label="Engineers in hard hats studying plans" style="background:linear-gradient(160deg,#e8e2d8,#6d7a86)"></div><p class="card-title">DIAM NUMMY NOLESTIE MOLESTIE</p><p class="card-sub">Interior</p></div>
    <div><div class="photo" role="img" aria-label="High-rise buildings under construction" style="background:linear-gradient(170deg,#4f86c6,#b08a5c)"></div><p class="card-title">DIAM NUMMY NOLESTIE MOLESTIE</p><p class="card-sub">Commercial</p></div>
    <div><div class="photo" role="img" aria-label="Builder at work on a scaffold" style="background:linear-gradient(170deg,#7fb2e0,#d19a52)"></div><p class="card-title">DIAM NUMMY NOLESTIE MOLESTIE</p><p class="card-sub">Exterior</p></div>
  </div>

  <span class="btn btn-blue view-all">VIEW ALL</span>

  <section class="contact">
    <h2 class="section-title">GET IN TOUCH</h2>
    <p class="contact-text">Lorem ipsum dolor sit amet, consectetur adipiscing elit, sed do eiusmod tempor incididunt ut labore et dolore magna aliqua. Ut enim ad minim veniam, quis nostrud exercitation ullamco laboris nisi ut aliquip.</p>
    <div class="details">
      <h4>CALL ME</h4><p>(555) 014-2368</p>
      <h4>EMAIL ME</h4><p>hello@pelicanbuilders.net</p>
      <h4>ADDRESS</h4><p>Pelican Builders LLC<br>PO Box 4821<br>Austin, TX 78700</p>
    </div>
    <div class="form">
      <span class="field" style="left:20px;top:20px;width:180px">NAME</span>
      <span class="field" style="left:20px;top:60px;width:180px">EMAIL</span>
      <span class="field" style="left:20px;top:100px;width:180px">SUBJECT</span>
      <span class="field" style="left:216px;top:20px;width:304px;height:80px">MESSAGE</span>
      <span class="btn btn-green">SEND NOW</span>
    </div>
    <p class="form-note">CONNECT WITH US TODAY FOR A FREE QUOTE</p>
  </section>

  <footer class="footer">
    <p>Copyright © 2015 yoursite All right reserved</p>
    <div class="social"><span></span><span></span><span></span><span></span></div>
  </footer>
</div>
</body>
</html>
```